willowcreekrestoring - healing business promotion

I have and energy / intuitive healing and kinesiology business. working with people who are looking for healing outside of the modern medical model, who have tried but failed in their search for understanding their conditions and why health and or happiness eludes them. the healing is done with love, patience and understanding. I am looking to be taken seriously with my presentation and to reach a person who may be deterred by the thought of angels and intuition! but to not exclude those that are attracted to that also.

Industry/Entity Type

Medical

Contact Information for Business Card

willowcreekrestoring
fast safe deep energy healing system
tamsin louise harte
energy healing / kinesiology and neurotraining
0417266183 07 4158 2746
home visits available for tarrin and ridgelands
t.lharte@quillmail.com

Requirements
Should not have
• Primary colours

```html
<!DOCTYPE html>
<html lang="en">
<head>
<meta charset="utf-8">
<title>willowcreekrestoring – tamsin louise harte</title>
<link href="https://fonts.googleapis.com/css2?family=Poiret+One&display=swap" rel="stylesheet">
<style>
  :root {
    --ink-light: #fdf1ea;
    --ink-soft: #f8e2d6;
    --ink-deep: #b42c3c;
    --paper: #ffffff;
    --glow-pink: #dfa3bb;
    --amber: #ef8a4a;
    --orange: #e9573a;
    --ember: #cf3a30;
    --wine: #b33444;
    --mist: #c07080;
  }
  * { margin: 0; padding: 0; box-sizing: border-box; }
  html, body { width: 1200px; height: 741px; overflow: hidden; background: var(--paper); }
  body { font-family: "Poiret One", sans-serif; }

  .card { position: relative; width: 1200px; height: 741px; background: var(--paper); }

  .artwork {
    position: absolute; left: 0; top: 0; width: 1200px; height: 649px;
    background:
      radial-gradient(ellipse 260px 110px at 540px 0px, var(--glow-pink) 0%, rgba(223,163,187,0) 100%),
      radial-gradient(ellipse 420px 180px at 560px 40px, rgba(239,138,74,0.9) 0%, rgba(239,138,74,0) 100%),
      radial-gradient(ellipse 520px 200px at 700px 620px, rgba(192,112,128,0.75) 0%, rgba(192,112,128,0) 100%),
      radial-gradient(ellipse 120px 70px at 600px 500px, rgba(245,150,90,0.6) 0%, rgba(245,150,90,0) 100%),
      linear-gradient(180deg, var(--amber) 0%, var(--orange) 25%, var(--ember) 55%, var(--wine) 85%, var(--mist) 100%);
  }

  .contact {
    position: absolute; left: 32px; top: 12px;
    list-style: none; color: var(--ink-soft);
    font-size: 30px; line-height: 42px; letter-spacing: 0.03em;
  }

  .practitioner {
    position: absolute; right: 20px; top: 236px; text-align: right; color: var(--ink-light);
  }
  .practitioner-name { font-size: 60px; font-weight: 400; letter-spacing: 0.22em; line-height: 64px; margin-right: -12px; }
  .practitioner-role { font-size: 29px; letter-spacing: 0.1em; line-height: 34px; margin-right: -2px; }

  .tagline {
    position: absolute; left: 36px; top: 502px;
    color: var(--ink-light); font-size: 110px; font-weight: 400;
    letter-spacing: 0.08em; line-height: 120px; white-space: nowrap;
    display: flex; align-items: center;
  }
  .tagline-dot {
    display: inline-block; width: 12px; height: 12px; margin: 18px 10px 0;
    border-radius: 50%; background: #fff;
    box-shadow: 0 0 8px 4px rgba(255,240,230,0.8);
  }

  .offer {
    position: absolute; left: 0; top: 656px; width: 1140px; text-align: center;
    color: var(--ink-deep); font-size: 31px; letter-spacing: 0.07em; line-height: 40px;
  }
</style>
</head>
<body>
<main class="card">
  <div class="artwork" role="img" aria-label="Warm orange and crimson abstract backdrop with soft swirling spiral marks drifting across it"></div>

  <ul class="contact">
    <li>0417 266 183</li>
    <li>07 4158 2746</li>
    <li>t.lharte@quillmail.com</li>
  </ul>

  <header class="practitioner">
    <h1 class="practitioner-name">tamsin louise harte</h1>
    <p class="practitioner-role">energy healing / kinesiology and neurotraining</p>
  </header>

  <p class="tagline">willow<span class="tagline-dot"></span>creek<span class="tagline-dot"></span>restoring</p>

  <p class="offer">fast safe deep energy healing system<br>home visit available for tarrin and ridgelands</p>
</main>
</body>
</html>
```